Lawn Company needs design work on a service call flyer!

We are a lawn care company that fertilizes and sprays lawns. This design is meant to be left behind at the customers house after a lawn application has been done too let them know what we have done.

The finished design will be printed on A6 paper (4.1 x 5.8 inches)

I have attached PDF files of the text that I want on the front of the document and the back of the document. I also included a sample design that I had been working on to give some idea what I would like. I don't want the same design, but you can use it as a building block for something new or come up with something entirely different.

FRONT: The front of the design is most important.

BACK: Other then the text the design should be minimal. If possible I would like an outline of the trees in my logo to be a backdrop. I have attached a PDF of the back of my business card as an example

The winning design will be a professional looking document that flows and reflects a lawn care business. Please contact me if you have any questions. I will only pick a design that is better then my current template.

Thank You

Target Market(s)

Lawn Care Customers

Industry/Entity Type

Lawn Care

Requirements
Must have
• 1. Our Logo
• 2. The attached text for the front & back of document
• 3. Our phone number (555-418-7390)
• 4. Our Email address (hollowfernturf@mailpost.example)
Nice to have
• A green theme with flowing graphics
Should not have
• any pictures of houses, people, or tools
• Don't copy the text or design from my design template. It is outdated, is it meant to be an example only

```html
<!DOCTYPE html>
<html lang="en">
<head>
<meta charset="utf-8">
<title>Hollowfern Turf – Service Call Card</title>
<link href="https://fonts.googleapis.com/css2?family=Source+Sans+3:ital,wght@0,400;0,600;0,700;1,400&display=swap" rel="stylesheet">
<style>
  :root{
    --stage:#dfe4dc;
    --leaf:#8cc63f;
    --leaf-deep:#2e7d1f;
    --forest:#1f5c14;
    --ink-green:#1e5a12;
    --mint:#eef6dc;
    --white:#ffffff;
    --grass-a:#3f8a25;
    --grass-b:#6bb33a;
  }
  *{box-sizing:border-box;margin:0;padding:0}
  html,body{width:1200px;height:800px;overflow:hidden}
  body{background:var(--stage);font-family:"Source Sans 3",sans-serif;position:relative}

  .card{position:absolute;top:198px;width:570px;height:404px;overflow:hidden;box-shadow:0 2px 8px rgba(0,0,0,.18)}
  .card--front{left:20px}
  .card--back{left:610px;background:var(--white)}

  /* FRONT */
  .front-backdrop{position:absolute;inset:0;background:radial-gradient(circle at 20% 25%,#c9ec7a 0,#7fc23a 35%,#3f8f22 100%)}
  .front-grass{position:absolute;left:0;right:0;bottom:0;height:70px;background:linear-gradient(to top,var(--grass-a),var(--grass-b) 70%,rgba(107,179,58,0))}
  .service-panel{position:absolute;left:178px;width:222px;top:0;height:330px;background:linear-gradient(#f4faea,#dcefc0);border-left:7px solid var(--forest);border-right:7px solid var(--forest);clip-path:polygon(0 0,100% 0,100% 82%,50% 100%,0 82%)}
  .brand{display:flex;align-items:center;justify-content:center;gap:8px;margin-top:34px}
  .brand-dot{width:22px;height:22px;border-radius:50%;background:var(--leaf-deep)}
  .brand-name{font-weight:700;font-size:22px;color:var(--forest)}
  .panel-field{margin:34px 18px 0;color:var(--forest);font-weight:600;font-size:15px;text-align:center}
  .fill-line{height:1px;background:var(--forest);margin:22px 8px 0}
  .panel-serviced{margin-top:26px;text-align:center;color:var(--forest);font-weight:600;font-size:15px;line-height:1.2}

  .applied-list{position:absolute;left:20px;top:150px;width:150px;color:var(--white)}
  .applied-list h2{font-weight:400;font-size:15px;line-height:1.15;margin-bottom:12px}
  .check-item{display:flex;gap:8px;margin-bottom:10px;font-size:13px;line-height:1.15}
  .check-box{flex:none;width:14px;height:14px;background:var(--white);margin-top:2px}
  .check-note{display:block;font-size:9.5px;margin-top:2px}
  .other-line{flex:1;border-bottom:1px solid var(--white);margin-bottom:3px}
  .watering-note{position:absolute;left:20px;right:180px;bottom:62px;display:flex;gap:6px;color:var(--white);font-size:13px;align-items:flex-end}

  .promise{position:absolute;left:418px;top:150px;width:136px;color:var(--white);font-style:italic;font-size:13px;line-height:1.35}

  /* BACK */
  .guide-header{height:46px;background:var(--leaf);color:var(--white);font-size:15.5px;padding:16px 22px 0}
  .guide-columns{display:flex;gap:22px;padding:12px 22px 0}
  .guide-col{flex:1;color:var(--ink-green)}
  .guide-col h3{color:var(--leaf-deep);font-weight:600;font-size:12.5px;margin-bottom:4px}
  .guide-intro{font-size:10.5px;line-height:1.25;margin-bottom:10px}
  .guide-col ul{padding-left:12px}
  .guide-col li{font-size:8.4px;line-height:1.3;margin-bottom:4px}
  .tree-band{position:absolute;right:28px;bottom:56px;width:360px;height:86px;background:linear-gradient(90deg,#4f9a2c,#3d8a22 50%,#5ea835);border-radius:40px 40px 4px 4px;opacity:.9}
  .contact-bar{position:absolute;left:0;right:0;bottom:0;height:54px;background:linear-gradient(#4f9d2b,#3c8420);display:flex;align-items:center;justify-content:center;gap:40px;color:var(--white);font-size:17px;font-weight:600}
  .contact-item{display:flex;align-items:center;gap:8px}
  .contact-item svg{width:30px;height:30px}
</style>
</head>
<body>

<section class="card card--front">
  <div class="front-backdrop" role="img" aria-label="Soft green bokeh lawn photograph"></div>
  <div class="front-grass" role="img" aria-label="Close-up of grass blades"></div>

  <div class="service-panel">
    <div class="brand"><span class="brand-dot"></span><span class="brand-name">Hollowfern Turf</span></div>
    <p class="panel-field">Application Time / Date:</p>
    <div class="fill-line"></div>
    <p class="panel-serviced">Your Lawn<br>has been Professionally<br>Serviced today by:</p>
    <div class="fill-line"></div>
  </div>

  <div class="applied-list">
    <h2>Today's application consists of:</h2>
    <div class="check-item"><span class="check-box"></span><span>Seasonally Balanced Slow Release Fertilizer</span></div>
    <div class="check-item"><span class="check-box"></span><span>Broadleaf Weed Control<span class="check-note">(Please keep off the lawn until it is thoroughly dry)</span></span></div>
    <div class="check-item"><span class="check-box"></span><span>Other:</span><span class="other-line"></span></div>
  </div>

  <div class="watering-note"><span>Please begin watering the lawn</span><span class="other-line"></span></div>

  <p class="promise">“We strive to complete work in a professional manner each and every visit to your home.”</p>
</section>

<section class="card card--back">
  <div class="guide-header">For best results please follow these general guidelines:</div>
  <div class="guide-columns">
    <div class="guide-col">
      <h3>WATERING YOUR LAWN</h3>
      <p class="guide-intro">When rainfall is not sufficient to meet your lawns watering needs, follow these guidelines for a lush green lawn</p>
      <ul>
        <li>Your lawn requires approx. 1 - 1.5 inches of water per week, sometimes more in hot, dry weather</li>
        <li>Avoid short frequent watering. It is best to water deeply once every 5 - 7 days. This encourages deep root growth.</li>
        <li>You can use a Frisbee or an empty tuna can to measure the amount you have watered. Just place it in the path of the sprinkler and when it is full, move your sprinkler to a new location.</li>
        <li>Aerating your lawn once a year will help your lawn utilize more water and prevent unnecessary runoff.</li>
      </ul>
    </div>
    <div class="guide-col">
      <h3>MOWING YOUR LAWN</h3>
      <p class="guide-intro">Mowing your lawn properly can make all the difference in how it looks throughout the year</p>
      <ul>
        <li>You should mow your lawn at 2.5 - 3 inches (no shorter). Mowing at this length helps shade your roots and provides more leaf surface for your lawn to manufacture its own food. As an added bonus it will help your lawn retain its moisture and reduce watering requirements.</li>
        <li>As a general rule, try not to remove more then 1/3 of the leave blade in a single mowing. During periods of heavy growth, this may mean mowing more frequently then usual.</li>
        <li>Always ensure your lawn mower is maintained and the blade is sharp so that is cuts cleanly.</li>
        <li>Your last mowing in the fall should be shorter, about 2 inches.</li>
      </ul>
    </div>
  </div>

  <div class="tree-band" role="img" aria-label="Row of four green grass-textured tree silhouettes through the seasons"></div>

  <div class="contact-bar">
    <span class="contact-item">
      <svg viewBox="0 0 30 30" aria-hidden="true"><circle cx="15" cy="15" r="13" fill="none" stroke="#fff" stroke-width="2"/><path d="M10 8l3 0 1.5 4-2 1.5c1 2 2.5 3.5 4.5 4.5l1.5-2 4 1.5v3c0 1-1 1.5-2 1.5C14 21.5 8.5 16 8.5 9.5 8.5 8.5 9 8 10 8z" fill="#fff"/></svg>
      555-418-7390
    </span>
    <span class="contact-item">
      <svg viewBox="0 0 30 30" aria-hidden="true"><circle cx="15" cy="15" r="13" fill="none" stroke="#fff" stroke-width="2"/><rect x="8" y="10" width="14" height="10" fill="none" stroke="#fff" stroke-width="1.8"/><path d="M8 10l7 6 7-6" fill="none" stroke="#fff" stroke-width="1.8"/></svg>
      hollowfernturf@mailpost.example
    </span>
  </div>
</section>

</body>
</html>
```